Little league sponsor banner

I need a banner designed for my sponsorship of a little league. The banner will be printed on a magnet and placed on all of the field score boards. The size of the banner will be 4 feet wide by 21 inches tall
Ive got an idea of what it needs to say I just need help with the design.
Ive uploaded our logo and my simple idea for the banner.
Id like colors to mostly be black white and subtle gold.
I can add anything that would enhance this. Headshots, real estate images, baseball images.
Im not creative at all so dont know how to do this.
I also uploaded an example of the one someone used last year.
I haven’t gotten my revisions
Industry/Entity Type
Real Estate Management
Look and feel
Each slider illustrates characteristics of the customer's brand and the style your logo design should communicate.

```html
<!DOCTYPE html>
<html lang="en">
<head>
<meta charset="utf-8">
<title>KEL Property Management – League Sponsor Banner</title>
<link href="https://fonts.googleapis.com/css2?family=Alegreya:wght@500;700;800&family=Montserrat:wght@700&display=swap" rel="stylesheet">
<style>
  :root {
    --stage: #4f4f4f;
    --paper: #ffffff;
    --ink: #111111;
    --gold-pale: #f4e29c;
    --gold-soft: #f7eab4;
    --gold-mid: #e2c867;
    --gold-deep: #c9a41a;
    --photo-navy: #1f2c52;
    --photo-green: #1f7a5a;
  }
  * { box-sizing: border-box; margin: 0; padding: 0; }
  html, body { width: 1200px; height: 646px; overflow: hidden; background: var(--stage); }
  body { position: relative; font-family: "Alegreya", Georgia, serif; color: var(--ink); }

  .banner {
    position: absolute; left: 108px; top: 111px;
    width: 974px; height: 426px;
    background: var(--paper); overflow: hidden;
  }

  .brand {
    position: absolute; left: 153px; top: 58px; width: 291px;
    text-align: center; font-weight: 800; color: var(--ink);
  }
  .brand-name { font-size: 64px; line-height: 1; letter-spacing: 2px; }
  .brand-sub { font-size: 24px; line-height: 1.1; margin-top: 6px; }

  .headline-band {
    position: absolute; left: 0; top: 216px; width: 586px; height: 48px;
    background: var(--gold-pale); border-radius: 0 16px 16px 0;
    display: flex; align-items: center; padding-left: 27px;
  }
  .headline { font-size: 28px; font-weight: 800; white-space: nowrap; }

  .services { position: absolute; left: 22px; top: 278px; width: 560px; height: 90px; list-style: none; }
  .service {
    position: absolute; display: flex; align-items: center; gap: 10px;
    font-size: 22px; font-weight: 700; white-space: nowrap;
  }
  .service svg { width: 21px; height: 21px; flex: none; }

  .phone-icon {
    position: absolute; left: 15px; top: 376px; width: 42px; height: 42px;
    border-radius: 3px;
    background: linear-gradient(135deg, var(--gold-deep), var(--gold-pale));
    display: flex; align-items: center; justify-content: center;
  }
  .phone-icon svg { width: 22px; height: 22px; }
  .phone-number {
    position: absolute; left: 75px; top: 377px;
    font-family: "Montserrat", Arial, sans-serif; font-weight: 700;
    font-size: 35px; line-height: 42px; letter-spacing: 0.5px;
  }

  .tagline-band { position: absolute; left: 321px; top: 379px; width: 653px; height: 47px; }
  .tagline-band svg { position: absolute; inset: 0; width: 100%; height: 100%; }
  .tagline {
    position: absolute; left: 39px; top: 0; height: 47px;
    display: flex; align-items: center;
    font-size: 20.5px; font-weight: 700; white-space: nowrap;
  }

  .family-photo {
    position: absolute; left: 605px; top: 0; width: 369px; height: 315px;
    background:
      linear-gradient(180deg, transparent 0 92px, var(--gold-mid) 92px 315px);
  }
  .family-photo::after {
    content: ""; position: absolute; left: 0; top: 0; width: 100%; height: 100%;
    background: linear-gradient(90deg, var(--photo-navy) 0 45%, var(--photo-green) 45% 78%, var(--photo-navy) 78%);
    opacity: 0.85;
    clip-path: polygon(4% 100%, 4% 40%, 15% 25%, 25% 20%, 50% 10%, 60% 5%, 80% 25%, 100% 30%, 100% 100%);
  }

  .caption-pill {
    position: absolute; top: 306px; height: 26px;
    background: var(--gold-pale); border-radius: 13px;
    display: flex; align-items: center; justify-content: center;
    font-size: 17px; font-weight: 700; white-space: nowrap;
  }
  .caption-year {
    position: absolute; top: 332px; font-size: 33px; font-weight: 800;
    text-align: center; transform: translateX(-50%);
  }
</style>
</head>
<body>
  <main class="banner">
    <div class="brand">
      <div class="brand-name">KEL</div>
      <div class="brand-sub">Property Management</div>
    </div>

    <div class="headline-band">
      <p class="headline">Proudly Supporting CVLL for&nbsp; over 30 years</p>
    </div>

    <ul class="services">
      <li class="service" style="left:0;top:4px"><svg viewBox="0 0 24 24"><circle cx="11" cy="13" r="9" fill="none" stroke="#d4af37" stroke-width="2.4"/><path d="M6.5 12.5l4 4L21 4" fill="none" stroke="#d4af37" stroke-width="2.6" stroke-linecap="round"/></svg>Single Family</li>
      <li class="service" style="left:182px;top:4px"><svg viewBox="0 0 24 24"><circle cx="11" cy="13" r="9" fill="none" stroke="#d4af37" stroke-width="2.4"/><path d="M6.5 12.5l4 4L21 4" fill="none" stroke="#d4af37" stroke-width="2.6" stroke-linecap="round"/></svg>Multi-family</li>
      <li class="service" style="left:356px;top:4px"><svg viewBox="0 0 24 24"><circle cx="11" cy="13" r="9" fill="none" stroke="#d4af37" stroke-width="2.4"/><path d="M6.5 12.5l4 4L21 4" fill="none" stroke="#d4af37" stroke-width="2.6" stroke-linecap="round"/></svg>Commercial</li>
      <li class="service" style="left:0;top:45px"><svg viewBox="0 0 24 24"><circle cx="11" cy="13" r="9" fill="none" stroke="#d4af37" stroke-width="2.4"/><path d="M6.5 12.5l4 4L21 4" fill="none" stroke="#d4af37" stroke-width="2.6" stroke-linecap="round"/></svg>Management</li>
      <li class="service" style="left:182px;top:45px"><svg viewBox="0 0 24 24"><circle cx="11" cy="13" r="9" fill="none" stroke="#d4af37" stroke-width="2.4"/><path d="M6.5 12.5l4 4L21 4" fill="none" stroke="#d4af37" stroke-width="2.6" stroke-linecap="round"/></svg>Leasing</li>
      <li class="service" style="left:356px;top:45px"><svg viewBox="0 0 24 24"><circle cx="11" cy="13" r="9" fill="none" stroke="#d4af37" stroke-width="2.4"/><path d="M6.5 12.5l4 4L21 4" fill="none" stroke="#d4af37" stroke-width="2.6" stroke-linecap="round"/></svg>Maintenance</li>
    </ul>

    <div class="phone-icon">
      <svg viewBox="0 0 24 24"><path d="M6.6 3.5l3 3.4-1.8 2.3c1.2 2.6 3.3 4.7 5.9 5.9l2.3-1.8 3.4 3-2 3.2C11 19.3 4.7 13 4.5 5.5z" fill="#111"/><path d="M14 5a6 6 0 0 1 5 5M14 2a9 9 0 0 1 8 8" fill="none" stroke="#111" stroke-width="1.6"/></svg>
    </div>
    <div class="phone-number">555.014.2270</div>

    <div class="tagline-band">
      <svg viewBox="0 0 653 47" preserveAspectRatio="none">
        <defs>
          <linearGradient id="bandGold" x1="0" x2="1">
            <stop offset="0" stop-color="#d1ab1e"/>
            <stop offset="0.35" stop-color="#f1dc8e"/>
            <stop offset="1" stop-color="#fbf1c6"/>
          </linearGradient>
        </defs>
        <polygon points="23,0 653,0 653,47 0,47" fill="url(#bandGold)"/>
      </svg>
      <p class="tagline">Family Owned and Operated, Serving North County since 1988</p>
    </div>

    <div class="family-photo" role="img" aria-label="Photo of a young ballplayer in 1995 beside two children in league uniforms in 2025, on a gold block"></div>

    <div class="caption-pill" style="left:627px;width:130px">Dan Merrow</div>
    <div class="caption-year" style="left:691px">1995</div>
    <div class="caption-pill" style="left:780px;width:186px">Sam and Lily Merrow</div>
    <div class="caption-year" style="left:875px">2025</div>
  </main>
</body>
</html>
```